Simple Logo Design for Semi-Clear Plastic Frosted Card stock

Create a business card on frosted plastic. compliment existing logo elements with a tree trunk, roots, or seed at the lower half and the full logo both on the front.

Contact information will go on a solid portion of the back of this design since this card stock is semi-transparent.

It is important to consider this plastic card stock medium in your design. I found helpful tips and guides listed at velnacard.example: be careful to understand ink printed on plastic cards cannot have too much of a consistent print area or risks peeling and fine lines can easily scratch off.
Updates

2" x 3.5" 20PT Clear Plastic Business cards with Round corners Please get info or templates here: https://www.velnacard.example/product-detail/2-x-35-20pt-clear-plastic-business-cards-with-round-corners

Target Market(s)

Not for profit- religion

Industry/Entity Type

Business

Contact Information for Business Card

Must include complementary elements to the existing logo

Font styles to use
Decorative

Colors
000000

Requirements
Must have
• Elements of community, nature and oneness. Such as: seed, roots, tree trunk, etc.
• Three lines of space on the back for Name, Title, Phone Number.
Nice to have
• I like a light use of decorative elements
Should not have
• No eyes, from faces or animals.

```html
<!DOCTYPE html>
<html lang="en">
<head>
<meta charset="utf-8">
<title>Steadfast Grove – Business Card</title>
<link rel="stylesheet" href="https://fonts.googleapis.com/css2?family=Josefin+Sans:wght@400;600&family=Roboto:wght@300;400&display=swap">
<style>
  :root {
    --backdrop: #e8e5e0;
    --frost: #eef0ef;
    --frost-edge: #d9dcdb;
    --deep-green: #0f3b35;
    --deep-green-light: #1a5148;
    --leaf-green: #2f6b2a;
    --brand-green: #1f4a3f;
    --gold-line: #c9b98a;
    --ink-light: #e6ece9;
    --ink-soft: #c7d3cf;
  }
  * { margin: 0; padding: 0; box-sizing: border-box; }
  html, body {
    width: 1200px;
    height: 969px;
    overflow: hidden;
    background: var(--backdrop);
  }
  .canvas {
    position: relative;
    width: 1200px;
    height: 969px;
  }
  .card {
    position: absolute;
    left: 120px;
    top: 210px;
    width: 960px;
    height: 549px;
    border-radius: 24px;
    box-shadow: 0 18px 40px rgba(0,0,0,0.18);
  }
  .card-art {
    position: absolute;
    inset: 0;
    width: 960px;
    height: 549px;
  }
  .brand {
    position: absolute;
    left: 82px;
    top: 288px;
    display: flex;
    flex-direction: column;
    align-items: flex-start;
  }
  .brand-row {
    display: flex;
    align-items: center;
    gap: 12px;
  }
  .brand-dot {
    width: 24px;
    height: 24px;
    border-radius: 50%;
    background: var(--brand-green);
  }
  .brand-name {
    font-family: "Josefin Sans", sans-serif;
    font-weight: 600;
    font-size: 32px;
    letter-spacing: 0.3px;
    color: var(--brand-green);
    line-height: 1;
    white-space: nowrap;
  }
  .brand-tagline {
    margin-top: 6px;
    margin-left: 36px;
    font-family: "Josefin Sans", sans-serif;
    font-weight: 600;
    font-size: 13px;
    letter-spacing: 1px;
    text-transform: uppercase;
    color: var(--brand-green);
    white-space: nowrap;
  }
  .contact {
    position: absolute;
    right: 61px;
    top: 200px;
    text-align: right;
    font-family: "Roboto", sans-serif;
    color: var(--ink-light);
    white-space: nowrap;
  }
  .contact-name {
    font-weight: 400;
    font-size: 34px;
    letter-spacing: 1.5px;
    text-transform: uppercase;
    line-height: 1.2;
  }
  .contact-title {
    margin-top: 4px;
    font-weight: 300;
    font-size: 28px;
    letter-spacing: 1px;
    text-transform: uppercase;
    color: var(--ink-soft);
    line-height: 1.2;
  }
  .contact-phone {
    margin-top: 26px;
    font-weight: 300;
    font-size: 28px;
    letter-spacing: 1.5px;
    color: var(--ink-soft);
    line-height: 1.2;
  }
</style>
</head>
<body>
<main class="canvas">
  <section class="card">
    <svg class="card-art" viewBox="0 0 960 549" xmlns="http://www.w3.org/2000/svg" aria-hidden="true">
      <defs>
        <clipPath id="card-shape">
          <rect x="0" y="0" width="960" height="549" rx="24" ry="24"/>
        </clipPath>
        <linearGradient id="frost-fill" x1="0" y1="0" x2="0" y2="1">
          <stop offset="0" stop-color="#f4f5f4"/>
          <stop offset="1" stop-color="#e3e6e5"/>
        </linearGradient>
        <linearGradient id="green-fill" x1="0" y1="0" x2="1" y2="1">
          <stop offset="0" stop-color="var(--deep-green-light)"/>
          <stop offset="1" stop-color="var(--deep-green)"/>
        </linearGradient>
      </defs>
      <g clip-path="url(#card-shape)">
        <rect class="frost-panel" x="0" y="0" width="960" height="549" fill="url(#frost-fill)"/>
        <path class="solid-panel" d="M452,0 C530,60 575,180 560,290 C545,410 440,500 315,549 L960,549 L960,0 Z" fill="url(#green-fill)"/>
        <path class="accent-line-green" d="M440,0 C518,60 563,180 548,290 C533,410 428,500 303,549" fill="none" stroke="var(--leaf-green)" stroke-width="4"/>
        <path class="accent-line-gold" d="M452,0 C530,60 575,180 560,290 C545,410 440,500 315,549" fill="none" stroke="var(--gold-line)" stroke-width="1.5"/>
      </g>
      <rect x="0.5" y="0.5" width="959" height="548" rx="24" ry="24" fill="none" stroke="var(--frost-edge)"/>
    </svg>

    <div class="brand">
      <div class="brand-row">
        <span class="brand-dot"></span>
        <span class="brand-name">STEADFAST GROVE</span>
      </div>
      <span class="brand-tagline">Rooted, Growing &amp; Whole</span>
    </div>

    <div class="contact">
      <p class="contact-name">Mara Linden</p>
      <p class="contact-title">President</p>
      <p class="contact-phone">555 0142 7788</p>
    </div>
  </section>
</main>
</body>
</html>
```